Business Card Design

I am a Building Surveyor and run my own Building Consultat company, providing professional advice and services to builders, architects, designers, owners, etc.

Industry/Entity Type

Business

Contact Information for Business Card

Dorwen Halket BBldgSurv (Hons)
Managing Director

57 Quillon Rise, Marrick Heights WA 6148
Mobile 0438 271 594
Email Dorwen.halket@tarnwellpq.com

Requirements
Must have
• I would like the back of the business card to be one colour (a shade of either black or maroon, matching the colours of my logo). Positioned in the centre on the back of the business card is to be my logo.

The front of the card is to be white, with my contact information in either black or maroon. The ADBldgSurv after my name should be in a smaller font size than my name. I would also like a small logo somewhere on this side of the card.

```html
<!DOCTYPE html>
<html lang="en">
<head>
<meta charset="utf-8">
<title>Tarnwell Building Consultants – Business Card</title>
<link href="https://fonts.googleapis.com/css2?family=Open+Sans:wght@400;600;700&display=swap" rel="stylesheet">
<style>
  :root {
    --canvas: #e9e7e4;
    --card-white: #ffffff;
    --card-black: #050505;
    --ink: #1a1a1a;
    --ink-soft: #333333;
    --maroon: #6b1f1a;
    --grey-mark: #8a8a8a;
    --rule: #b9a7a3;
  }
  * { box-sizing: border-box; margin: 0; padding: 0; }
  html, body { width: 1200px; height: 1000px; overflow: hidden; }
  body {
    background: var(--canvas);
    font-family: "Open Sans", Arial, sans-serif;
    color: var(--ink);
    position: relative;
  }
  .card {
    position: absolute;
    top: 336px;
    width: 540px;
    height: 328px;
    border-radius: 12px;
    box-shadow: 0 6px 18px rgba(0,0,0,0.18);
    overflow: hidden;
  }
  .card--front { left: 40px; background: var(--card-white); }
  .card--back { left: 620px; background: var(--card-black); }

  .brand {
    position: absolute;
    display: flex;
    align-items: center;
    gap: 10px;
  }
  .brand__dot {
    width: 40px; height: 40px;
    border-radius: 50%;
  }
  .brand__name {
    font-weight: 600;
    font-size: 21px;
    letter-spacing: 1.5px;
    line-height: 1.05;
    text-transform: uppercase;
  }
  .brand__name small {
    display: block;
    font-size: 9.5px;
    letter-spacing: 1.6px;
    font-weight: 600;
    margin-top: 3px;
  }
  .card--front .brand { left: 50%; top: 50px; transform: translateX(-50%); }
  .card--front .brand__dot { background: var(--maroon); }
  .card--front .brand__name { color: var(--ink-soft); }
  .card--back .brand { left: 50%; top: 50%; transform: translate(-50%, -50%); }
  .card--back .brand__dot { background: #ffffff; }
  .card--back .brand__name { color: #ffffff; }

  .divider {
    position: absolute;
    left: 20px; right: 0; top: 162px;
    height: 1px;
    background: linear-gradient(90deg, rgba(107,31,26,0.15), var(--maroon) 45%, rgba(107,31,26,0.25));
  }

  .person { position: absolute; left: 62px; top: 218px; }
  .person__name { font-size: 19px; font-weight: 700; color: var(--ink); }
  .person__title { font-size: 12.5px; color: var(--ink-soft); margin-top: 6px; margin-left: 6px; }

  .contacts {
    position: absolute;
    left: 290px; top: 206px;
    list-style: none;
    font-size: 12.5px;
    color: var(--ink-soft);
  }
  .contacts li { display: flex; align-items: center; gap: 8px; height: 25px; }
  .contacts svg { width: 15px; height: 15px; flex: none; }
</style>
</head>
<body>
  <section class="card card--front" aria-label="Business card front">
    <div class="brand">
      <span class="brand__dot"></span>
      <span class="brand__name">Tarnwell<small>Building Consultants</small></span>
    </div>
    <div class="divider"></div>
    <div class="person">
      <p class="person__name">Dorwen Halket</p>
      <p class="person__title">ADBldgSurv Director</p>
    </div>
    <ul class="contacts">
      <li>
        <svg viewBox="0 0 16 16" aria-hidden="true"><circle cx="8" cy="8" r="7.2" fill="none" stroke="#333" stroke-width="1.2"/><rect x="5.6" y="3.8" width="4.8" height="8.4" rx="0.8" fill="none" stroke="#333" stroke-width="1.1"/><circle cx="8" cy="10.7" r="0.6" fill="#333"/></svg>
        0438 271 594
      </li>
      <li>
        <svg viewBox="0 0 16 16" aria-hidden="true"><circle cx="8" cy="8" r="7.2" fill="#333"/><rect x="4" y="5.3" width="8" height="5.6" fill="#fff"/><path d="M4 5.3 L8 8.6 L12 5.3" fill="none" stroke="#333" stroke-width="0.9"/></svg>
        Dorwen.halket@tarnwellpq.com
      </li>
      <li>
        <svg viewBox="0 0 16 16" aria-hidden="true"><circle cx="8" cy="8" r="7.2" fill="#333"/><path d="M8 12.4 C6 9.8 5.2 8.6 5.2 7 A2.8 2.8 0 0 1 10.8 7 C10.8 8.6 10 9.8 8 12.4Z" fill="#fff"/><circle cx="8" cy="7" r="1" fill="#333"/></svg>
        57 Quillon Rise, Marrick Heights WA 6148
      </li>
    </ul>
  </section>

  <section class="card card--back" aria-label="Business card back">
    <div class="brand">
      <span class="brand__dot"></span>
      <span class="brand__name">Tarnwell<small>Building Consultants</small></span>
    </div>
  </section>
</body>
</html>
```